Brantham Carpets Ltd

I'm looking for a modern looking business card with a logo that's relates to the business, maybe a sheep etc. I will need my name and phone numbers to be included

Industry/Entity Type

Business

Contact Information for Business Card

Neil Brantham, Director
Phone numbers mobile 07931 642058 and office 0161 735 2846
Carpets and flooring supplied and fitted

```html
<!DOCTYPE html>
<html lang="en">
<head>
<meta charset="utf-8">
<title>Brantham Carpets Ltd – Business Card</title>
<link href="https://fonts.googleapis.com/css2?family=Quicksand:wght@400;500;700&display=swap" rel="stylesheet">
<style>
  :root {
    --blue: #3b8bd0;
    --blue-band: #3480c4;
    --charcoal: #333436;
    --charcoal-soft: #4a4b4e;
    --paper: #f1f2f3;
    --mark: #d9dadc;
    --white: #ffffff;
    --ink: #2c2d2f;
    --backdrop: #e4e5e7;
  }
  * { box-sizing: border-box; margin: 0; padding: 0; }
  html, body {
    width: 1200px; height: 800px; overflow: hidden;
    background: var(--backdrop);
    font-family: "Quicksand", sans-serif;
  }
  .canvas { position: relative; width: 1200px; height: 800px; }
  .card {
    position: absolute; top: 245px;
    width: 540px; height: 310px; overflow: hidden;
    box-shadow: 0 6px 18px rgba(0,0,0,0.18);
  }

  /* Front */
  .card--front { left: 40px; background: var(--blue); }
  .front__band {
    position: absolute; left: 0; top: 70px; width: 100%; height: 105px;
    background: var(--charcoal);
  }
  .front__strip {
    position: absolute; left: 0; top: 175px; width: 100%; height: 42px;
    background: var(--blue-band);
  }
  .front__mark {
    position: absolute; left: 244px; top: 78px;
    width: 52px; height: 52px; border-radius: 50%;
    background: var(--mark);
  }
  .front__name {
    position: absolute; left: 0; top: 136px; width: 100%;
    text-align: center; color: var(--white);
    font-weight: 500; font-size: 25px; letter-spacing: 1px;
  }
  .front__tagline {
    position: absolute; left: 0; top: 184px; width: 100%;
    text-align: center; color: var(--white);
    font-weight: 500; font-size: 16px; letter-spacing: 0.5px;
  }

  /* Back */
  .card--back { left: 620px; background: var(--paper); }
  .back__shapes { position: absolute; inset: 0; }
  .back__brand {
    position: absolute; left: 30px; top: 62px;
    display: flex; align-items: center; gap: 12px;
  }
  .back__mark {
    width: 34px; height: 34px; border-radius: 50%;
    background: var(--mark);
  }
  .back__name {
    color: var(--blue); font-weight: 500; font-size: 22px; letter-spacing: 1px;
  }
  .back__person {
    position: absolute; right: 34px; top: 112px; text-align: right;
  }
  .person__name { color: var(--ink); font-size: 19px; font-weight: 500; }
  .person__name strong { font-weight: 700; }
  .person__role { color: var(--blue); font-size: 13px; font-weight: 500; }
  .back__contact {
    position: absolute; left: 26px; top: 192px;
    display: flex; align-items: flex-start; gap: 12px;
  }
  .contact__icon { width: 26px; height: 26px; flex: none; }
  .contact__lines { color: var(--white); font-size: 16px; line-height: 20px; }
  .contact__lines b { font-weight: 700; }
</style>
</head>
<body>
<main class="canvas">
  <section class="card card--front">
    <div class="front__band"></div>
    <div class="front__strip"></div>
    <div class="front__mark"></div>
    <p class="front__name">BRANTHAM CARPETS LTD</p>
    <p class="front__tagline">Carpets and flooring supplied and fitted</p>
  </section>

  <section class="card card--back">
    <svg class="back__shapes" width="540" height="310" viewBox="0 0 540 310">
      <path d="M0 175 H400 Q432 175 432 207 V310 H0 Z" fill="var(--charcoal)"/>
      <path d="M0 262 H320 C370 262 372 222 425 222 H540 V310 H0 Z" fill="var(--blue)"/>
    </svg>
    <div class="back__brand">
      <span class="back__mark"></span>
      <span class="back__name">BRANTHAM CARPETS LTD</span>
    </div>
    <div class="back__person">
      <p class="person__name">Neil <strong>Brantham</strong></p>
      <p class="person__role">Director</p>
    </div>
    <div class="back__contact">
      <svg class="contact__icon" viewBox="0 0 26 26" aria-hidden="true">
        <rect width="26" height="26" rx="4" fill="var(--charcoal-soft)"/>
        <path d="M6 11 Q13 5 20 11 L18 13 L16 11.5 L16 10 Q13 9 10 10 L10 11.5 L8 13 Z" fill="var(--white)"/>
        <rect x="8" y="14" width="10" height="6" rx="1.5" fill="var(--white)"/>
      </svg>
      <div class="contact__lines">
        <p><b>mobile</b>: 07931 642058</p>
        <p><b>office</b>: 0161 735 2846</p>
      </div>
    </div>
  </section>
</main>
</body>
</html>
```